I need a website built for my modeling agency company.

On our website, a user can create a profile and we will submit it to thousands of modeling agents throughout the country.

In many cases, they will receive multiple offers from modeling agencies which allows them to pick and choose the contract that is best for them to launch their modeling career.

Some tag lines to consider using:

"Submit your profile to hundreds of modeling agents instantly!"

"Get found and become a star!"

We are: The Runway Guild.

Our Slogan: The World''s Largest Network of Fashion Models and Agents

What We Do: We are an agency with one of the largest networks of fashion professionals that are looking for new modeling talent. We host professional profiles for aspiring models, professional fashion models seeking work, modeling talent seekers, and top modeling agencies. We connect aspiring models with the top modeling agencies in the United States and abroad.

By submitting your FREE profile, you will be instantly introduced to the industry’s leading modeling agents. Within a few days, you could receive multiple, competing offers from modeling agencies that all want to launch your modeling career. Receiving multiple signing offers puts you in control of deciding which contract best suites you!

Reason: I've seen some good designs, but none that are 100% perfect. These are the ones that I like best so far (to give you some ideas): http://files.pixelvane.example/img/510372/820114/820114_4917263_510372_image.jpg http://files.pixelvane.example/img/510372/829305/829305_4926851_510372_image.jpg http://files.pixelvane.example/img/510372/51847/51847_4924097_510372_image.jpg http://files.pixelvane.example/img/510372/51847/51847_4919856_510372_image.jpg http://files.pixelvane.example/img/510372/823670/823670_4920438_510372_image.jpg

Target Market(s)

Aspiring models (mostly female, but some male)

Industry/Entity Type

Modeling Agency

Colors

Designer to choose colors to be used in the design.

Requirements
Nice to have
• Somewhere in the top half of the page, I would like there to be a small form for the visitor to fill out. This form will look as follows:

Title: Instantly contact hundreds of modeling agents who are looking for new talent and could make you a star!
Fields: First Name*, Last Name*, Age, Zip Code, Email Address*, Daytime Phone, Evening Phone, Comments.

Then, there will be a "submit" button to proceed to next step of form. Just below the "submit" button, should be the following verbiage: "You will have the opportunity to upload photo(s) and provide other pertinent information in next step."

```html
<!DOCTYPE html>
<html lang="en">
<head>
<meta charset="utf-8">
<title>The Runway Guild</title>
<link rel="stylesheet" href="https://fonts.googleapis.com/css2?family=Montserrat:ital,wght@0,600;0,800;1,800&family=Open+Sans:ital,wght@0,400;0,700;1,400&display=swap">
<style>
:root{
  --bg:#141414;
  --nav:#0c0c0c;
  --pink:#e5007d;
  --white:#ffffff;
  --grey:#8a8a8a;
  --grey-dark:#3b3b3b;
  --text-small:#9c9c9c;
}
*{margin:0;padding:0;box-sizing:border-box}
html,body{width:1200px;height:2392px;overflow:hidden;background:var(--bg)}
body{position:relative;font-family:"Open Sans",Arial,sans-serif;color:var(--white)}
.abs{position:absolute}
.heading{font-family:"Montserrat",Arial,sans-serif;font-weight:800;text-transform:uppercase;line-height:.95}
.pink{color:var(--pink)}
.white{color:var(--white)}
.small{font-size:11px;line-height:1.5;color:var(--text-small);text-transform:uppercase}
.backdrop{position:absolute;left:0;top:0}

/* nav */
.site-nav{position:absolute;left:0;top:0;width:1200px;height:56px;background:var(--nav);border-bottom:1px solid #2a2a2a}
.brand{position:absolute;left:150px;top:0;height:56px;display:flex;align-items:center;gap:10px}
.brand-mark{width:22px;height:22px;background:var(--white)}
.brand-name{font-family:"Montserrat",sans-serif;font-weight:600;font-size:14px;color:var(--white);text-transform:uppercase;letter-spacing:1px;white-space:nowrap}
.menu{position:absolute;left:380px;top:0;height:56px;display:flex;align-items:center;gap:34px;list-style:none}
.menu li{font-family:"Montserrat",sans-serif;font-weight:600;font-size:13px;letter-spacing:1px}
.search-field{position:absolute;left:1010px;top:16px;width:150px;height:24px;border:1px solid #444;background:#1b1b1b;font-size:11px;color:#777;padding:4px 8px}

/* photo areas */
.photo{position:absolute}
.hero-photo{left:290px;top:57px;width:440px;height:960px;background:radial-gradient(ellipse 55% 45% at 50% 38%,#8a5a3e 0%,#4a2c1f 45%,rgba(20,20,20,0) 85%)}
.silhouette-area{left:830px;top:690px;width:140px;height:210px;background:radial-gradient(ellipse 50% 55% at 50% 50%,rgba(229,0,125,.85) 0%,rgba(229,0,125,.35) 60%,rgba(229,0,125,0) 100%)}
.phone{left:270px;top:1600px;width:130px;height:270px;border-radius:20px;background:linear-gradient(#2d2d2d,#111);border:3px solid #555}
.runway{left:600px;top:1540px;width:340px;height:260px;background:linear-gradient(160deg,#2a2a35 0%,#5a5060 45%,#1a1a1a 100%)}
.cover-model{left:820px;top:1900px;width:380px;height:492px;background:radial-gradient(ellipse at 55% 35%,#9a6b58 0%,#4d2c3a 40%,#151515 85%)}

/* feature tiles */
.tile{position:absolute;top:1090px;width:140px;height:180px;border:5px solid var(--pink);background:linear-gradient(#4b3b44,#191919)}
.tile-label{position:absolute;left:0;right:0;top:60px;text-align:center;font-family:"Montserrat",sans-serif;font-weight:800;font-size:16px;line-height:1.05;color:var(--white);text-transform:uppercase}
.tile-label span{color:var(--pink)}

.play{position:absolute;left:700px;top:1650px;font-family:"Montserrat",sans-serif;font-weight:800;font-style:italic;font-size:36px;color:var(--pink)}
.link-more{font-family:"Montserrat",sans-serif;font-weight:600;font-size:12px;color:var(--pink);text-transform:uppercase}
</style>
</head>
<body>

<svg class="backdrop" width="1200" height="2392" viewBox="0 0 1200 2392" aria-hidden="true">
  <polygon points="560,56 1200,56 1200,620 780,1000 380,1000" fill="#1f1f1f"/>
  <polygon points="0,56 560,56 380,1000 0,760" fill="#181818"/>
  <polygon points="380,1000 780,1000 1200,620 1200,1000 360,1070" fill="#262626"/>
  <polygon points="0,1380 1200,1380 1200,1420 0,1560" fill="#1d1d1d"/>
  <polygon points="0,1900 560,1900 820,2392 0,2392" fill="#181818"/>
  <line x1="380" y1="1000" x2="1200" y2="620" stroke="#333" stroke-width="2"/>
</svg>

<nav class="site-nav">
  <div class="brand"><span class="brand-mark"></span><span class="brand-name">The Runway Guild</span></div>
  <ul class="menu">
    <li>Home</li><li>About</li><li>Contact</li><li>News</li><li>Register</li><li>Login</li>
  </ul>
  <div class="search-field">Search</div>
</nav>

<!-- hero -->
<div class="photo hero-photo" role="img" aria-label="Portrait photo of the featured model"></div>
<div class="abs heading" style="left:90px;top:190px;width:190px;text-align:right;font-size:26px">
  <div class="white">My<br>name is</div>
  <div style="color:var(--grey);font-size:20px;margin-top:4px">Lena<br>Moreau</div>
</div>
<div class="abs heading" style="left:580px;top:96px;width:580px;text-align:center;font-size:62px">
  <div class="pink">I am a</div>
  <div><span class="white">World</span><span class="pink">class</span></div>
  <div class="white">Model</div>
</div>
<p class="abs" style="left:680px;top:400px;width:480px;font-size:12px;line-height:1.55;color:var(--text-small)">I was born in a small town and always dreamed of the runway. At sixteen I created my free profile with The Runway Guild, and within days agents from top agencies were calling me. Today I work with leading fashion houses and travel the world doing what I love.</p>
<p class="abs" style="left:900px;top:570px;width:260px;text-align:right;font-size:13px;color:var(--pink);font-style:italic;line-height:1.4">The Runway Guild<br>changed my life</p>

<!-- aspiring models -->
<div class="abs heading" style="left:620px;top:690px;font-size:50px">
  <div class="pink">Aspir</div><div class="pink">ing</div><div class="white">Mod</div><div class="white">els</div>
</div>
<div class="photo silhouette-area" role="img" aria-label="Pink silhouette of a model"></div>

<div class="abs link-more" style="left:380px;top:1010px;color:var(--grey)">Search now</div>
<p class="abs small" style="left:620px;top:1005px;width:240px">Submit your profile to hundreds of modeling agents instantly. Get found by leading agencies.</p>
<p class="abs small" style="left:890px;top:1005px;width:260px">Creating your profile is free. Add photos and let top agencies come to you.</p>

<div class="tile" style="left:380px" role="img" aria-label="Photo of featured models"><div class="tile-label">Meet<br><span>the</span><br>models</div></div>
<div class="tile" style="left:580px" role="img" aria-label="Photo from a fashion event"><div class="tile-label">Upcoming<br><span>events</span></div></div>
<div class="tile" style="left:780px" role="img" aria-label="Photo from the media gallery"><div class="tile-label">Media<br><span>gallery</span></div></div>

<!-- slogan and cam -->
<div class="abs heading" style="left:140px;top:1400px;width:600px;font-size:38px;color:var(--grey-dark);font-style:italic">The world's largest network of fashion models and agents</div>
<div class="abs heading" style="left:760px;top:1440px;width:140px;font-size:28px;text-align:center"><div class="white">The</div><div><span class="pink">Ava</span> <span class="white">cam</span></div></div>
<p class="abs small" style="left:920px;top:1400px;width:240px;text-align:right">Follow Ava Laurent backstage at fashion week and see what a day on the runway is really like.</p>

<div class="abs heading" style="left:140px;top:1600px;font-size:24px;line-height:1">
  <div class="white">The</div><div class="pink">Runway</div><div class="pink">Guild</div><div class="white">App</div>
</div>
<div class="photo phone" role="img" aria-label="Phone showing the mobile app"></div>
<div class="abs link-more" style="left:140px;top:1850px;color:var(--grey)">Download ›</div>
<div class="photo runway" role="img" aria-label="Runway show photo"></div>
<div class="play">Play</div>

<!-- news -->
<div class="abs heading pink" style="left:420px;top:1750px;font-size:32px;font-style:italic">News</div>
<p class="abs small" style="left:420px;top:1810px;width:180px"><span style="color:var(--white)">Spring casting call opens for new faces</span><br>Posted 2 days ago</p>
<p class="abs small" style="left:620px;top:1810px;width:190px"><span style="color:var(--white)">Guild members sign with top Paris agency</span><br>Posted 5 days ago</p>
<div class="abs link-more" style="left:720px;top:1870px">All news »</div>

<!-- connections -->
<div class="abs heading" style="left:230px;top:1940px;font-size:22px;line-height:1">
  <div class="pink">Connections</div><div class="white">with <span class="pink">the top</span></div><div class="white">modeling</div><div class="pink">agencies</div>
</div>
<div class="abs link-more" style="left:480px;top:2060px;color:var(--grey)">Find more</div>

<div class="photo cover-model" role="img" aria-label="Model posing in evening wear"></div>

<!-- footer -->
<div class="abs" style="left:180px;top:2170px;display:flex;align-items:center;gap:12px">
  <span style="width:30px;height:30px;background:var(--white);display:block"></span>
  <span class="brand-name" style="font-size:22px">The Runway Guild</span>
</div>
<p class="abs" style="left:180px;top:2212px;font-size:11px;color:var(--text-small)">The World's Largest Network of Fashion Models and Agents</p>
<p class="abs small" style="left:180px;top:2260px;width:260px">The Runway Guild<br>1200 Harbor Ave, Suite 400<br>New York, NY 10011<br>Tel 555-0142<br>hello@runwayguild.example</p>
<p class="abs small" style="left:540px;top:2260px;width:160px">Privacy Policy<br>Terms of Use<br>Careers<br>Site Map</p>
<div class="abs heading" style="left:840px;top:2240px;width:320px;text-align:right;font-size:18px;line-height:1.1">
  <div class="pink">Separate talent</div><div class="white">agencies &amp; modeling</div><div class="pink">talent agents</div>
</div>

</body>
</html>
```